Roof Plumbing Company needs simple, modern business card using the attached logo and below details:

Dean Halloway
Summit Gutters Pty Ltd
ABN: 58 214 937 062
Phone: 0417 286 531
Email: summitgutters@mailbrook.com
Website: summitgutters.com.au

For all of your metal roof plumbing requirements contact Summit Gutters for an obligation free quote - no job too big or to small!

Industry/Entity Type

Business

Contact Information for Business Card

Dean Halloway
Summit Gutters Pty Ltd
ABN 58 214 937 062
0417 286 531
summitgutters@mailbrook.com
summitgutters.com.au

Requirements
Must have
• Bright eye catching design, professional look

```html
<!DOCTYPE html>
<html lang="en">
<head>
<meta charset="utf-8">
<title>Summit Gutters Pty Ltd – Business Card</title>
<link rel="stylesheet" href="https://fonts.googleapis.com/css2?family=Montserrat:wght@400;500;700&display=swap">
<style>
  :root {
    --backdrop: #1d1d1f;
    --card-white: #ffffff;
    --brand-red: #e0232a;
    --charcoal: #414143;
    --light-grey: #e2e1e3;
    --text-white: #ffffff;
  }
  * { box-sizing: border-box; margin: 0; padding: 0; }
  html, body {
    width: 1200px;
    height: 800px;
    overflow: hidden;
    background: var(--backdrop);
    font-family: "Montserrat", sans-serif;
  }
  .canvas {
    position: relative;
    width: 1200px;
    height: 800px;
  }
  .card {
    position: absolute;
    width: 540px;
    height: 320px;
    background: var(--card-white);
    overflow: hidden;
  }

  /* Front */
  .card-front { left: 600px; top: 60px; }
  .card-front .edge-arrow {
    position: absolute;
    top: 50%;
    transform: translateY(-50%);
    width: 40px;
    height: 90px;
  }
  .card-front .edge-arrow.left { left: 0; }
  .card-front .edge-arrow.right { right: 0; }

  .wordmark {
    display: flex;
    align-items: center;
    gap: 12px;
    color: var(--brand-red);
    font-weight: 700;
    letter-spacing: 0.04em;
    text-transform: uppercase;
  }
  .wordmark .mark-square {
    width: 22px;
    height: 22px;
    background: var(--brand-red);
    flex: none;
  }
  .card-front .wordmark {
    position: absolute;
    left: 0; right: 0; top: 0; bottom: 0;
    justify-content: center;
    font-size: 30px;
    line-height: 1.05;
  }

  /* Back */
  .card-back { left: 60px; top: 420px; }
  .panel { position: absolute; }
  .panel-grey   { left: 0;     top: 0;     width: 245px; height: 180px; background: var(--light-grey); }
  .panel-logo   { left: 245px; top: 0;     width: 295px; height: 180px; background: var(--card-white);
                  display: flex; align-items: center; justify-content: center; }
  .panel-contact{ left: 0;     top: 180px; width: 245px; height: 110px; background: var(--brand-red);
                  padding: 30px 0 0 22px; }
  .panel-name   { left: 245px; top: 180px; width: 295px; height: 96px;  background: var(--charcoal);
                  padding: 24px 0 0 22px; }
  .strip-dark   { left: 0;     top: 290px; width: 245px; height: 30px;  background: var(--charcoal); }
  .strip-red    { left: 245px; top: 276px; width: 295px; height: 44px;  background: var(--brand-red); }

  .panel-logo .wordmark { font-size: 22px; line-height: 1.05; gap: 10px; }
  .panel-logo .mark-square { width: 18px; height: 18px; }

  .contact-list {
    list-style: none;
    color: var(--text-white);
    font-size: 11.5px;
    font-weight: 500;
    line-height: 1.45;
    text-transform: uppercase;
    letter-spacing: 0.02em;
  }
  .person-name {
    color: var(--text-white);
    font-size: 21px;
    font-weight: 700;
    letter-spacing: 0.02em;
    text-transform: uppercase;
  }
  .person-abn {
    color: var(--text-white);
    font-size: 17px;
    font-weight: 400;
    letter-spacing: 0.03em;
    margin-top: 2px;
  }
</style>
</head>
<body>
<main class="canvas">

  <section class="card card-front" aria-label="Business card front">
    <svg class="edge-arrow left" viewBox="0 0 40 90" aria-hidden="true">
      <polygon points="0,0 40,45 0,90" fill="var(--brand-red)"/>
    </svg>
    <div class="wordmark">
      <span class="mark-square"></span>
      <span>Summit Gutters<br>Pty Ltd</span>
    </div>
    <svg class="edge-arrow right" viewBox="0 0 40 90" aria-hidden="true">
      <polygon points="40,0 0,45 40,90" fill="var(--brand-red)"/>
    </svg>
  </section>

  <section class="card card-back" aria-label="Business card back">
    <div class="panel panel-grey"></div>
    <div class="panel panel-logo">
      <div class="wordmark">
        <span class="mark-square"></span>
        <span>Summit Gutters<br>Pty Ltd</span>
      </div>
    </div>
    <div class="panel panel-contact">
      <ul class="contact-list">
        <li>0417 286 531</li>
        <li>summitgutters@mailbrook.com</li>
        <li>summitgutters.com.au</li>
      </ul>
    </div>
    <div class="panel panel-name">
      <p class="person-name">Dean Halloway</p>
      <p class="person-abn">ABN 58 214 937 062</p>
    </div>
    <div class="panel strip-dark"></div>
    <div class="panel strip-red"></div>
  </section>

</main>
</body>
</html>
```